Tavrelo.com.au - AV and Communications Installation Company Website

A company website for a modern, high level/enterprise communications installation/engineering company based in Sydney Australia.
My client base is construction companies working in medical, government and educations departments so the website needs to look professional.
Clients like Quenby or Dorvik as I want to eventually move into data centre design and installation so I need something appealing to the high end market.
Fiber Optic Installation is a massive part of the company aswell.
Audio visual, IT installation is also what the company will be involved in.
I want the website to be modern, eye catching, professional looking.

Target Market(s)

High end clients and construction companies

Industry/Entity Type

Communications

Coding

Coded - Design and coding required

Number of Pages Required

1 page

Requirements
Must have
• Modern and clean layout with links to other social media platforms

```html
<!DOCTYPE html>
<html lang="en">
<head>
<meta charset="utf-8">
<title>Tavrelo – AV and Communications Installation</title>
<link href="https://fonts.googleapis.com/css2?family=Roboto:ital,wght@0,300;0,400;0,500;0,700;1,300&display=swap" rel="stylesheet">
<style>
:root{
  --teal:#1a97a6;
  --teal-bright:#1cbfca;
  --teal-dark:#13707c;
  --ink:#1c1c1c;
  --muted:#6f6f6f;
  --line:#e4e4e4;
  --panel:#f4f4f4;
  --footer:#0c2b33;
  --footer-bar:#176877;
  --white:#ffffff;
}
*{box-sizing:border-box;margin:0;padding:0}
html,body{width:1200px;height:2256px;overflow:hidden}
body{position:relative;background:var(--white);font-family:'Roboto',sans-serif;color:var(--ink)}
.abs{position:absolute}
a{color:inherit;text-decoration:none}

/* top bar */
.topbar{left:0;top:0;width:1200px;height:33px;border-bottom:1px solid var(--line)}
.topbar .cell{top:0;height:33px;display:flex;align-items:center;gap:7px;font-size:11px;color:#8a8a8a;border-left:1px solid var(--line);padding-left:14px}
.topbar .social{top:0;height:33px;width:34px;border-left:1px solid var(--line);display:flex;align-items:center;justify-content:center}
.topbar .social span{width:8px;height:8px;border:1px solid #999;border-radius:50%}

/* nav */
.brand{left:162px;top:46px;font-size:34px;font-weight:500;color:var(--teal);letter-spacing:1px;display:flex;align-items:center;gap:8px}
.brand i{display:block;width:14px;height:14px;background:var(--teal);border-radius:50%}
.nav{top:58px;left:604px;display:flex;gap:16px;font-size:13px;color:#444}
.quote-btn{left:950px;top:52px;width:88px;height:28px;background:var(--teal);color:#fff;font-size:10px;font-weight:500;display:flex;align-items:center;justify-content:center;border-radius:2px}

/* hero */
.hero{left:0;top:98px;width:1200px;height:900px;background:linear-gradient(180deg,#5a5650 0%,#7d7468 35%,#a09888 60%,#d8d4ce 85%,#ffffff 100%)}
.hero-title{left:0;top:192px;width:1200px;text-align:center;font-size:52px;font-weight:700;color:#fff}
.hero-sub{left:350px;top:270px;width:500px;text-align:center;font-size:19px;line-height:31px;font-weight:300;color:#fff}
.btn{top:360px;width:136px;height:43px;display:flex;align-items:center;justify-content:center;font-size:12px;font-weight:500}
.btn-light{left:460px;background:#fff;color:var(--teal)}
.btn-teal{left:604px;background:var(--teal);color:#fff}

/* services */
.services{left:96px;top:506px;width:1008px;height:589px;border-radius:8px;background:linear-gradient(180deg,#178f9c 0%,#18a7b3 60%,#1ab8c3 85%,#1697a5 100%)}
.sec-title{left:0;top:540px;width:1200px;text-align:center;font-size:35px;font-weight:500;color:#fff}
.sec-sub{left:0;top:586px;width:1200px;text-align:center;font-size:14px;color:#d9f3f5}
.card{top:652px;width:278px;height:307px;border-radius:4px;overflow:hidden}
.card .ttl{position:absolute;left:0;bottom:33px;width:100%;text-align:center;color:#fff;font-size:15px;font-weight:500}
.card .more{position:absolute;left:0;bottom:17px;width:100%;text-align:center;color:#fff;font-size:10px}
.c1{left:159px;background:linear-gradient(160deg,#2a6fc0,#2c8ad8 45%,#b9a94a 75%,#1d2a3e)}
.c2{left:460px;background:linear-gradient(180deg,#d9dde0,#a9b0b6 55%,#2a3138)}
.c3{left:760px;background:linear-gradient(180deg,#e7eef3,#c9a45a 45%,#d2683a 60%,#3c4a5e)}
.arrow{top:790px}
.cable{left:96px;top:915px;width:290px;height:230px;background:radial-gradient(ellipse at 55% 55%,#c9ccd0 0%,#b0b4b8 35%,rgba(255,255,255,0) 70%)}

/* about */
.about-left{left:161px;top:1183px;width:544px;height:297px;background:var(--panel)}
.about-right{left:705px;top:1183px;width:333px;height:297px;background:var(--teal)}
.about-lead{left:190px;top:1209px;width:470px;font-size:19px;line-height:26px;color:#111}
.about-body{left:190px;top:1307px;width:470px;font-size:13.5px;line-height:24.8px;font-weight:300;color:#555}
.about-title{left:764px;top:1219px;font-size:29px;font-weight:500;color:#fff}
.about-rule{left:764px;top:1266px;width:223px;height:2px;background:#fff}
.about-quote{left:764px;top:1285px;width:245px;font-size:23.5px;line-height:33px;font-style:italic;font-weight:300;color:#fff}
.circle{left:680px;top:1304px}

/* projects */
.proj-title{left:0;top:1539px;width:1200px;text-align:center;font-size:31px;font-weight:500;color:#111}
.proj-rule{left:569px;top:1591px;width:60px;height:2px;background:var(--teal)}
.tab{top:1628px;height:24px;text-align:center;font-size:13px;font-weight:500;color:#333;border-bottom:1px solid #ccc}
.tab.active{color:var(--teal);border-bottom:2px solid var(--teal)}
.project{top:1682px;width:277px;height:257px;border:1px solid var(--line)}
.project .img{height:215px}
.project .cap{height:42px;display:flex;align-items:center;justify-content:center;font-size:14px;font-weight:500;color:#222;letter-spacing:.2px}
.p1{left:161px}.p1 .img{background:linear-gradient(160deg,#4a5260,#2f7fd0 50%,#8b6a55)}
.p2{left:462px}.p2 .img{background:linear-gradient(180deg,#e9ecef 0%,#c8d0d6 30%,#a5442c 60%,#7a8c90 100%)}
.p3{left:761px}.p3 .img{background:linear-gradient(180deg,#eef1f3,#b9c5cc 60%,#525a62)}

/* footer */
.footer{left:0;top:1998px;width:1200px;height:218px;background:var(--footer)}
.f-head{top:2042px;font-size:15px;font-weight:500;color:#fff}
.f-rule{top:2069px;width:37px;height:2px;background:var(--teal-bright)}
.f-text{left:162px;top:2080px;width:170px;font-size:10.5px;line-height:17.5px;font-weight:300;color:#b9c8cc}
.f-list{top:2094px;list-style:none;font-size:11px;color:#b9c8cc}
.f-list li{height:26.5px;display:flex;align-items:flex-start;gap:8px}
.f-list li::before{content:"";width:4px;height:4px;background:#b9c8cc;margin-top:5px}
.f-contact{left:837px;top:2095px;font-size:11px;color:#b9c8cc;list-style:none}
.f-contact li{height:31px;display:flex;gap:10px;align-items:flex-start}
.bottombar{left:0;top:2216px;width:1200px;height:40px;background:var(--footer-bar);color:#d5e8eb;font-size:11.5px}
.bottombar .copy{position:absolute;left:162px;top:12px}
.bottombar .links{position:absolute;right:160px;top:12px;display:flex;gap:14px}
.bottombar .links u{color:#fff}
</style>
</head>
<body>

<header>
  <div class="abs topbar"></div>
  <div class="abs topbar cell" style="left:162px;width:194px;border-bottom:none">
    <svg width="12" height="10" viewBox="0 0 12 10"><rect x=".5" y=".5" width="11" height="9" fill="none" stroke="#999"/><path d="M.5 .5 6 5.5 11.5 .5" fill="none" stroke="#999"/></svg>
    info@tavrelo.com.au
  </div>
  <div class="abs topbar cell" style="left:355px;width:154px;border-bottom:none;border-right:1px solid var(--line)">
    <svg width="12" height="12" viewBox="0 0 12 12"><path d="M2 1 4 1 5 4 3.5 5a7 7 0 0 0 3.5 3.5L8 7l3 1v2a1 1 0 0 1-1 1A9 9 0 0 1 1 2a1 1 0 0 1 1-1z" fill="none" stroke="#999"/></svg>
    700-555-0148
  </div>
  <a class="abs social" style="left:937px" href="#" aria-label="Chatterly"><span></span></a>
  <a class="abs social" style="left:971px" href="#" aria-label="Pictaro"><span></span></a>
  <a class="abs social" style="left:1005px;border-right:1px solid var(--line)" href="#" aria-label="Linkbook"><span></span></a>

  <div class="abs brand"><i></i>TAVRELO</div>
  <nav class="abs nav"><a href="#">Home</a><a href="#">About Us</a><a href="#">Services</a><a href="#">Our Work</a><a href="#">Contact Us</a></nav>
  <a class="abs quote-btn" href="#">GET A QUOTE</a>
</header>

<section>
  <div class="abs hero" role="img" aria-label="Photo of a technician in a hard hat working on a server cabinet"></div>
  <h1 class="abs hero-title">Welcome to Tavrelo</h1>
  <p class="abs hero-sub">Lorem Ipsum is simply dummy text of the printing and typesetting industry. Lorem Ipsum.</p>
  <a class="abs btn btn-light" href="#">OUR SERVICES</a>
  <a class="abs btn btn-teal" href="#">ABOUT US</a>
</section>

<section>
  <div class="abs services"></div>
  <h2 class="abs sec-title">Our Services</h2>
  <p class="abs sec-sub">Lorem Ipsum is simply dummy text</p>

  <div class="abs card c1" role="img" aria-label="Photo of network patch panel with fibre cables">
    <div class="ttl">IT Installation</div><div class="more">Learn More</div>
  </div>
  <div class="abs card c2" role="img" aria-label="Photo of circuit breakers in a switchboard">
    <div class="ttl">Audio visual</div><div class="more">Learn More</div>
  </div>
  <div class="abs card c3" role="img" aria-label="Photo of a worker in a safety vest laying cable beside machinery">
    <div class="ttl">Fiber Optic Installation</div><div class="more">Learn More</div>
  </div>

  <svg class="abs arrow" style="left:172px" width="16" height="30" viewBox="0 0 16 30"><path d="M14 2 2 15l12 13" fill="none" stroke="#fff" stroke-width="2.5"/></svg>
  <svg class="abs arrow" style="left:1012px" width="16" height="30" viewBox="0 0 16 30"><path d="M2 2l12 13L2 28" fill="none" stroke="#fff" stroke-width="2.5"/></svg>

  <div class="abs cable" role="img" aria-label="Photo of a grey cable with round connectors"></div>
</section>

<section>
  <div class="abs about-left"></div>
  <div class="abs about-right"></div>
  <p class="abs about-lead">Tavrelo are a highly skilled engineering organisation operating throughout NSW across all sectors of the construction and services industries.</p>
  <p class="abs about-body">Lorem Ipsum is simply dummy text of the printing and typesetting industry. Lorem Ipsum has been the industry's standard dummy text ever since the 1500s, when an unknown printer took a galley of type and scrambled it to make a type specimen book. It has survived not only five centuries, but also the leap into electronic typesetting, remaining essentially unchanged.</p>
  <svg class="abs circle" width="56" height="56" viewBox="0 0 56 56"><circle cx="28" cy="28" r="26" fill="var(--teal)" stroke="#fff" stroke-width="4"/><circle cx="28" cy="28" r="17" fill="none" stroke="#fff" stroke-width="1.5"/><path d="M20 28h16M30 22l6 6-6 6" fill="none" stroke="#fff" stroke-width="1.5"/></svg>
  <h2 class="abs about-title">ABOUT TAVRELO</h2>
  <div class="abs about-rule"></div>
  <p class="abs about-quote">At Tavrelo we pride ourselves on providing our clients with high-quality installations at competitive industry rates.</p>
</section>

<section>
  <h2 class="abs proj-title">RECENT PROJECTS</h2>
  <div class="abs proj-rule"></div>
  <div class="abs tab active" style="left:392px;width:38px">All</div>
  <div class="abs tab" style="left:453px;width:99px">Medical</div>
  <div class="abs tab" style="left:575px;width:98px">Government</div>
  <div class="abs tab" style="left:695px;width:112px">Education</div>

  <div class="abs project p1"><div class="img" role="img" aria-label="Photo of hands crimping blue network cables"></div><div class="cap">Lorem Ipsum is simply dummy text</div></div>
  <div class="abs project p2"><div class="img" role="img" aria-label="Photo of a modern brick school building"></div><div class="cap">Typesetting industry</div></div>
  <div class="abs project p3"><div class="img" role="img" aria-label="Photo of a hospital operating theatre"></div><div class="cap">Remaining essentially unchanged</div></div>
</section>

<footer>
  <div class="abs footer"></div>
  <h3 class="abs f-head" style="left:162px">Tavrelo.com.au</h3>
  <h3 class="abs f-head" style="left:387px">Services</h3>
  <h3 class="abs f-head" style="left:612px">Follow Us</h3>
  <h3 class="abs f-head" style="left:837px">Contact Info</h3>
  <div class="abs f-rule" style="left:162px"></div>
  <div class="abs f-rule" style="left:387px"></div>
  <div class="abs f-rule" style="left:612px"></div>
  <div class="abs f-rule" style="left:837px"></div>
  <p class="abs f-text">Lorem Ipsum is simply dummy text of the printing and typesetting industry. Lorem Ipsum has been the industry's standard dummy text ever since the 1500s, when</p>
  <ul class="abs f-list" style="left:387px"><li>Fiber Optic Installation</li><li>Audio Visual</li><li>IT Installation</li></ul>
  <ul class="abs f-list" style="left:612px"><li>Chatterly</li><li>Pictaro</li><li>Linkbook</li></ul>
  <ul class="abs f-contact">
    <li><svg width="12" height="9" viewBox="0 0 12 9"><rect width="12" height="9" fill="#b9c8cc"/><path d="M0 0l6 5 6-5" fill="none" stroke="#0c2b33"/></svg>info@tavrelo.com.au</li>
    <li><svg width="12" height="12" viewBox="0 0 12 12"><path d="M2 1 4 1 5 4 3.5 5a7 7 0 0 0 3.5 3.5L8 7l3 1v2a1 1 0 0 1-1 1A9 9 0 0 1 1 2a1 1 0 0 1 1-1z" fill="#b9c8cc"/></svg>000-555-0190</li>
    <li><svg width="12" height="12" viewBox="0 0 12 12"><circle cx="6" cy="6" r="5.5" fill="#b9c8cc"/><path d="M.5 6h11M6 .5c-3 3-3 8 0 11M6 .5c3 3 3 8 0 11" fill="none" stroke="#0c2b33" stroke-width=".8"/></svg>www.tavrelo.com.au</li>
  </ul>
  <div class="abs bottombar">
    <span class="copy">©&nbsp; Copyright 2020 All Right Reserved.</span>
    <span class="links"><u>Privacy Statement</u><span>|</span><span>Terms Of Use</span></span>
  </div>
</footer>

</body>
</html>
```